Software Company Business Card Design

We are looking for a business card design for a software, messaging & IT services company based in Australia.

Talvora Group is the holding company for 3 brands all offering technology based business solutions; Talvora, Brindle & Quillpad. Brand Identity = Friendly, Professional, Viable, Vibrant, Creative

We want our business card to reflect that we are an innovative market leader. The design should be clean, professional and original.

This design will be used for all 3 brands.

More information about our company can be found at: www.talvoragroup.example.au
www.brindle.example.au

Details we would like on the card:

Firstname Lastname
Position
Level 17, 482 Ormond Rd
North Sydney
NSW 2060
Phone: +61 2 5550 1738
Fax: +61 2 5550 1794
Mobile:
Email:
www.talvoragroup.example.au

Target Market(s)

Our business cards are given to B2B and industry professionals.

Industry/Entity Type

Business

Requirements
Must have
• The Business Card must include the same colours as the logo.
Nice to have
• We would like it to me double sided.

```html
<!DOCTYPE html>
<html lang="en">
<head>
<meta charset="utf-8">
<title>Talvora Group – Business Card</title>
<link rel="stylesheet" href="https://fonts.googleapis.com/css2?family=Roboto:wght@300;400;700&display=swap">
<style>
  :root {
    --page: #ffffff;
    --card: #0d0b0c;
    --pattern-a: #2a2023;
    --pattern-b: #1a1416;
    --accent-red: #c8173a;
    --accent-lilac: #a6a1cf;
    --text-light: #f2f2f2;
    --text-muted: #bdbdbd;
  }
  * { margin: 0; padding: 0; box-sizing: border-box; }
  html, body {
    width: 1200px; height: 1200px; overflow: hidden;
    background: var(--page);
    font-family: "Roboto", Arial, sans-serif;
  }
  .canvas { position: relative; width: 1200px; height: 1200px; }
  .card {
    position: absolute; left: 91px; width: 1018px;
    background: var(--card); overflow: hidden;
  }
  .card--front { top: 19px; height: 569px; }
  .card--back { top: 612px; height: 581px; }

  .card__pattern {
    position: absolute; inset: 0;
    background: radial-gradient(ellipse at 55% 45%, var(--pattern-a) 0%, var(--pattern-b) 55%, var(--card) 100%);
  }
  .card__pattern--back {
    inset: 0 0 auto 0; height: 260px;
    background: linear-gradient(180deg, var(--pattern-b) 0%, var(--card) 100%);
  }

  .brand {
    position: absolute; left: 0; right: 0; top: 205px;
    display: flex; align-items: center; justify-content: center; gap: 34px;
  }
  .brand__dot {
    width: 96px; height: 96px; border-radius: 50%;
    background: var(--accent-lilac);
  }
  .brand__name {
    color: var(--text-light); font-weight: 700;
    font-size: 124px; line-height: 1; letter-spacing: -2px;
  }

  .person {
    position: absolute; right: 41px; top: 648px;
  }
  .person, .address, .contact, .website { position: absolute; }
  .person { top: 36px; text-align: right; }
  .person__name { color: var(--accent-red); font-size: 48px; font-weight: 300; line-height: 60px; }
  .person__role { color: var(--text-muted); font-size: 32px; font-weight: 300; line-height: 46px; }

  .address { left: 48px; top: 215px; color: var(--text-light); font-size: 36px; font-weight: 300; line-height: 50.5px; }
  .contact { left: 511px; top: 215px; font-size: 36px; font-weight: 300; line-height: 50.5px; list-style: none; }
  .contact__label { color: var(--accent-red); }
  .contact__value { color: var(--text-light); }

  .website {
    left: 0; right: 0; top: 500px; text-align: center;
    color: var(--accent-red); font-size: 31px; font-weight: 300;
  }
</style>
</head>
<body>
<main class="canvas">
  <section class="card card--front" aria-label="Card front">
    <div class="card__pattern" role="img" aria-label="Faint repeated brand name pattern in dark tones"></div>
    <div class="brand">
      <span class="brand__dot"></span>
      <span class="brand__name">Talvora Group</span>
    </div>
  </section>

  <section class="card card--back" aria-label="Card back">
    <div class="card__pattern card__pattern--back" role="img" aria-label="Faint repeated brand name pattern in dark tones"></div>
    <div class="person">
      <p class="person__name">Firstname Lastname</p>
      <p class="person__role">Position</p>
    </div>
    <address class="address" style="font-style: normal;">
      Level 17, 482 Ormond Rd<br>
      North Sydney<br>
      NSW 2060
    </address>
    <ul class="contact">
      <li><span class="contact__label">Phone:</span> <span class="contact__value">+61 2 5550 1738</span></li>
      <li><span class="contact__label">Fax:</span> <span class="contact__value">+61 2 5550 1794</span></li>
      <li><span class="contact__label">Mobile:</span></li>
      <li><span class="contact__label">Email:</span></li>
    </ul>
    <p class="website">www.talvoragroup.example.au</p>
  </section>
</main>
</body>
</html>
```